furniture and home contents restoration

I need to list the services that we perform in our studio.
we serve the general public as well as the insurance/ remediation industry

```html
<!DOCTYPE html>
<html lang="en">
<head>
<meta charset="utf-8">
<title>Ashgrove Refinishers – Business Card</title>
<link href="https://fonts.googleapis.com/css2?family=PT+Serif:ital,wght@0,400;0,700;1,400&family=Jost:wght@400;500;600&family=Arimo:wght@400&display=swap" rel="stylesheet">
<style>
  :root {
    --navy: #0b1230;
    --orange: #f57f0f;
    --paper: #f4f4f4;
    --ink: #1c1c1c;
    --backdrop: #e7e4df;
    --text-light: #eef0f6;
  }
  * { box-sizing: border-box; margin: 0; padding: 0; }
  html, body {
    width: 1200px; height: 900px; overflow: hidden;
    background: var(--backdrop);
  }
  .canvas {
    position: relative; width: 1200px; height: 900px;
  }
  .card {
    position: absolute; left: 250px; width: 700px; height: 400px;
    overflow: hidden;
    box-shadow: 0 6px 18px rgba(0,0,0,0.18);
  }
  .card--front { top: 30px; background: var(--paper); }
  .card--back { top: 470px; background: var(--navy); }

  /* front */
  .front__header {
    position: absolute; left: 0; top: 0; width: 100%; height: 152px;
    background: var(--navy); color: #fff;
  }
  .brand {
    position: absolute; right: 34px; top: 18px; text-align: right;
  }
  .brand__name {
    font-family: "PT Serif", serif; font-weight: 700;
    font-size: 50px; line-height: 1; letter-spacing: 0.5px;
  }
  .brand__sub {
    font-family: "PT Serif", serif; font-size: 15px;
    letter-spacing: 1.6px; margin-top: 2px;
  }
  .tagline {
    position: absolute; left: 34px; right: 28px; bottom: 14px;
    font-family: "PT Serif", serif; font-style: italic;
    font-size: 18.5px; letter-spacing: 0.6px; text-align: right;
  }
  .front__nameband {
    position: absolute; left: 0; top: 152px; width: 100%; height: 60px;
    background: var(--orange);
  }
  .person {
    position: absolute; left: 34px; top: 12px;
    font-family: "Jost", sans-serif; font-weight: 600;
    font-size: 30px; letter-spacing: 3px; color: #fff;
  }
  .address {
    position: absolute; right: 34px; top: 226px; text-align: right;
    font-family: "Jost", sans-serif; font-style: normal;
    font-size: 17px; line-height: 1.35;
    letter-spacing: 0.8px; color: var(--ink);
  }
  .contacts {
    position: absolute; left: 34px; top: 268px; list-style: none;
  }
  .contacts__item {
    display: flex; align-items: center; height: 38px;
    font-family: "Jost", sans-serif; font-size: 19px;
    letter-spacing: 1px; color: var(--ink);
  }
  .contacts__icon {
    width: 30px; height: 30px; border-radius: 50%;
    background: var(--orange); margin-right: 18px;
    display: flex; align-items: center; justify-content: center;
  }
  .contacts__icon svg { width: 16px; height: 16px; }
  .contacts__gap { display: inline-block; width: 18px; }

  /* back */
  .services {
    position: absolute; list-style: none;
    font-family: "Arimo", sans-serif; font-size: 15px; line-height: 21px;
    color: var(--text-light);
  }
  .services li { position: relative; padding-left: 18px; white-space: nowrap; }
  .services li::before {
    content: ""; position: absolute; left: 2px; top: 8px;
    width: 5px; height: 5px; border-radius: 50%; background: var(--text-light);
  }
  .services--left { left: 48px; top: 36px; }
  .services--right { left: 345px; top: 60px; }
  .back__rule {
    position: absolute; left: 48px; right: 48px; top: 284px;
    height: 2px; background: var(--text-light);
  }
  .back__footer {
    position: absolute; left: 0; right: 0; top: 302px; text-align: center;
    font-family: "Arimo", sans-serif; font-size: 17px; line-height: 24px;
    letter-spacing: 0.2px; color: var(--text-light); text-transform: uppercase;
  }
</style>
</head>
<body>
<main class="canvas">

  <section class="card card--front" aria-label="Business card front">
    <header class="front__header">
      <div class="brand">
        <div class="brand__name">Ashgrove Refinishers</div>
        <div class="brand__sub">HOME CONTENTS RESTORATION</div>
      </div>
      <p class="tagline">Serving The General Public And The Insurance Industry For Over 40 Years</p>
    </header>

    <div class="front__nameband">
      <h1 class="person">MARTIN DELACROIX</h1>
    </div>

    <address class="address">128 Linden Mill Road,<br>Brookhaven,<br>NY 10900</address>

    <ul class="contacts">
      <li class="contacts__item">
        <span class="contacts__icon">
          <svg viewBox="0 0 24 24" aria-hidden="true"><path fill="#fff" d="M6.6 10.8c1.4 2.8 3.8 5.1 6.6 6.6l2.2-2.2c.3-.3.7-.4 1-.2 1.1.4 2.3.6 3.6.6.6 0 1 .4 1 1V20c0 .6-.4 1-1 1C10.6 21 3 13.4 3 4c0-.6.4-1 1-1h3.5c.6 0 1 .4 1 1 0 1.3.2 2.5.6 3.6.1.3 0 .7-.2 1l-2.3 2.2z"/></svg>
        </span>
        O: 555-201-4400<span class="contacts__gap"></span>M: 555-318-2297
      </li>
      <li class="contacts__item">
        <span class="contacts__icon">
          <svg viewBox="0 0 24 24" aria-hidden="true"><path fill="#fff" d="M2 11.5 22 3l-6 18-4.5-6.5L2 11.5zm9.5 3 1.5 3.5 1-4.5 6-8-8.5 9z"/></svg>
        </span>
        studio@ashgroverefinish.com
      </li>
      <li class="contacts__item">
        <span class="contacts__icon">
          <svg viewBox="0 0 24 24" aria-hidden="true"><path fill="#fff" d="M7 3h10v4H7zM4 8h16a2 2 0 0 1 2 2v6h-4v5H6v-5H2v-6a2 2 0 0 1 2-2zm4 8v3h8v-3z"/></svg>
        </span>
        555-201-4410
      </li>
    </ul>
  </section>

  <section class="card card--back" aria-label="Business card back, list of services">
    <ul class="services services--left">
      <li>Antique Repair and Restoration</li>
      <li>Cleaning and Remounting</li>
      <li>Mirror Frame Repair</li>
      <li>Chandelier Cleaning and Restoration</li>
      <li>Document Restoration</li>
      <li>Ceramic, and Mirror Repair</li>
      <li>Repair and Restoration</li>
      <li>Shade Replacement</li>
      <li>Kitchen Removal and Reinstallation</li>
      <li>Cleaning and Restoration</li>
    </ul>
    <ul class="services services--right">
      <li>Metal Polishing and Restoration Art</li>
      <li>Photo Restoration</li>
      <li>Odor Removal and Ozone Services Art</li>
      <li>Upholstery Cleaning and Deodorizing</li>
      <li>In-House Upholstery and Reupholster Glass</li>
      <li>Rug Cleaning and Restoration Hardware</li>
      <li>Musical Instrument Restoration</li>
      <li>Window Treatment Repair/ Restoration Lamp</li>
      <li>Leather Restoration and Replacement Lamp</li>
      <li>Piano Restoration and Repair</li>
    </ul>
    <div class="back__rule"></div>
    <p class="back__footer">On-site inspections and desk review services<br>Assessment reports and estimates for repair and restoration</p>
  </section>

</main>
</body>
</html>
```